sailbuddies Website for children with diabilities

Hi, we are looking for a new website design for our community service "sailbuddies". Sailbuddies gives children who suffer from diseases or disabilities a week off on a Boat to give the children new hope and an unforgettable experience.

The current website is really old and we want to have a new one.
Please feel free to discover our website under http://sailbuddies-example.at/.
We have several company sponsors which are very important to us.

The Website has to be a Bootstrap Design (Version 4.4 or higher) [NOT Wordpress, Joomla, other CMS]

Target Market(s)

no target market. we like to inform our communities about our service.

Industry/Entity Type

community service for children with disabilities

Coding

Coded - Design and coding required

Number of Pages Required

4 page

Font styles to use
Sans Serif

Colors
0054AA
0677BA
7BADD7
CADEEF
E8F1F8
0094D4
00A9DD
6FCCEA
C7EBF8
E9F6FB

Requirements
Must have
• About, Sponsors, Information about cruises
Nice to have
• Gallery

```html
<!DOCTYPE html>
<html lang="en">
<head>
<meta charset="utf-8">
<title>Verein Sail Buddies</title>
<link rel="stylesheet" href="https://fonts.googleapis.com/css2?family=Fredoka:wght@500;600;700&family=Roboto:wght@400;500&display=swap">
<style>
:root{
  --navy:#1b1f5e;
  --blue:#0f8fd0;
  --button:#0c95d5;
  --grey-bg:#f1f1f1;
  --teal-bg:#e3f4f5;
  --text:#3a3a3a;
  --muted:#b4b4b4;
  --white:#ffffff;
}
*{margin:0;padding:0;box-sizing:border-box}
html,body{width:1200px;height:4498px;overflow:hidden}
body{position:relative;background:var(--white);font-family:"Roboto",sans-serif;color:var(--text)}
.abs{position:absolute}
.heading{font-family:"Fredoka",sans-serif;font-weight:600;color:var(--navy);letter-spacing:.3px}
.heading .accent{color:var(--blue)}
.body-copy{font-size:13.5px;line-height:20px;color:var(--text)}
.btn{position:absolute;display:flex;align-items:center;justify-content:center;background:var(--button);color:var(--white);font-family:"Fredoka",sans-serif;font-weight:600;font-size:16px;border-radius:20px}
.photo{position:absolute;overflow:hidden}

/* header */
.site-header{position:absolute;left:0;top:0;width:1200px;height:91px;background:var(--white);z-index:5}
.brand-mark{position:absolute;left:52px;top:28px;width:94px;height:94px;border-radius:50%;background:var(--navy);border:4px solid var(--white);z-index:6}
.brand-name{position:absolute;left:154px;top:34px;font-size:24px;color:var(--navy);font-family:"Roboto",sans-serif}
.main-nav a{position:absolute;top:38px;font-family:"Fredoka",sans-serif;font-weight:600;font-size:15px;color:var(--navy);text-decoration:none}

/* hero */
.hero-photo{left:0;top:91px;width:1200px;height:650px;background:linear-gradient(180deg,#c9dde8 0%,#a8c6d6 22%,#3d6d4a 26%,#4f7c8c 34%,#2f5f7c 60%,#2a5270 100%)}
.hero-circle{left:127px;top:192px;width:366px;height:366px;border-radius:50%;background:var(--navy);color:var(--white);text-align:center;z-index:3}
.hero-circle h2{font-family:"Fredoka",sans-serif;font-weight:600;font-size:32px;margin-top:70px}
.hero-circle p{font-size:11.5px;line-height:18.5px;width:250px;margin:14px auto 0}

.welcome-title{left:0;top:806px;width:1200px;text-align:center;font-size:54px}
.welcome-copy{left:212px;top:885px;width:776px;text-align:center;font-size:14px}

.about-title{left:149px;top:1108px;font-size:52px;color:var(--blue)}
.about-copy{left:149px;top:1188px;width:450px}

/* sponsors */
.sponsors-title{left:0;top:1620px;width:1200px;text-align:center;font-size:54px}
.sponsors-sub{left:0;top:1697px;width:1200px;text-align:center;font-family:"Fredoka",sans-serif;font-weight:600;font-size:22px;color:var(--muted)}
.ship-label{position:absolute;top:1760px;width:280px;text-align:center;font-family:"Fredoka",sans-serif;font-weight:600;font-size:20px;color:#c8c8c8}
.sponsor-card{position:absolute;width:280px;height:125px;background:var(--white);border-radius:16px;box-shadow:0 4px 18px rgba(0,0,0,.09);display:flex;align-items:center;justify-content:center;text-align:center;font-family:"Roboto",sans-serif;font-weight:500;font-size:28px;color:var(--navy)}
.arrow{position:absolute;top:2035px;width:48px;height:24px}

/* cruises */
.cruises-title{left:466px;top:2442px;font-size:52px}
.cruises-copy{left:466px;top:2522px;width:565px}
.feature-list{position:absolute;left:668px;top:2630px;list-style:none}
.feature-list li{display:flex;align-items:center;height:48px;font-family:"Fredoka",sans-serif;font-weight:600;font-size:23px;color:var(--navy)}
.feature-list svg{width:36px;height:30px;margin-right:8px}

/* gallery */
.gallery-title{left:0;top:3282px;width:1200px;text-align:center;font-size:56px}
.gallery-copy{left:330px;top:3370px;width:540px;text-align:center}
.gallery-item{position:absolute;width:284px;height:220px;border-radius:20px}

/* footer */
.footer-mark{left:550px;top:4180px;width:100px;height:100px;border-radius:50%;background:var(--navy);border:4px solid var(--white)}
.footer-name{left:0;top:4290px;width:1200px;text-align:center;font-size:24px;color:var(--white)}
.footer-nav{left:0;top:4350px;width:1200px;display:flex;justify-content:center;gap:36px;font-family:"Fredoka",sans-serif;font-weight:600;font-size:15px;color:var(--white)}
.copyright{left:0;top:4405px;width:1200px;text-align:center;font-family:"Fredoka",sans-serif;font-weight:600;font-size:14px;color:var(--white)}
</style>
</head>
<body>

<header class="site-header">
  <div class="brand-name">Verein <strong style="font-weight:500">Sail Buddies</strong></div>
  <nav class="main-nav">
    <a style="left:486px">Home</a>
    <a style="left:568px">Sponsors</a>
    <a style="left:672px">Fleet Info 2022</a>
    <a style="left:827px">Gallery</a>
    <a style="left:926px">Cruises</a>
  </nav>
  <div class="btn" style="left:1015px;top:31px;width:97px;height:35px;font-size:15px">Donate</div>
</header>
<div class="brand-mark"></div>

<!-- hero -->
<div class="photo abs hero-photo" role="img" aria-label="Smiling children in life jackets steering a motorboat across a lake with a skipper"></div>
<div class="abs" style="left:0;top:741px;width:1200px;height:720px;background:var(--grey-bg)"></div>
<svg class="abs" style="left:0;top:580px" width="1200" height="170" viewBox="0 0 1200 170">
  <path d="M0,31 C300,-20 500,160 700,155 C900,150 1050,40 1200,20 L1200,170 L0,170 Z" fill="#f1f1f1"/>
</svg>
<div class="abs hero-circle">
  <h2>We Are......</h2>
  <p>...trained social workers and experienced skippers who volunteer in the Sail Buddies association and organize a fleet every year for socially disadvantaged children and young people from central Upper Austria and set up the necessary financial resources.</p>
</div>
<div class="btn" style="left:254px;top:458px;width:116px;height:39px;z-index:4">Donate</div>

<!-- welcome -->
<h1 class="abs heading welcome-title">Welcome to <span class="accent">Sail Buddies</span></h1>
<p class="abs body-copy welcome-copy">...enabling children and young people who don't always have it easy in life to spend an unforgettable week in Croatia. It is precisely this shared experience that gives the children and young people a new zest for life and perspectives for their future. Through the reflection and also the care afterwards in the individual facilities, the children and young people can draw on this experience for a long time to come. This sustainability creates numerous pedagogical points of contact that represent a valuable basis for the achievement of goals.</p>

<!-- about -->
<h2 class="abs heading about-title">About Us</h2>
<p class="abs body-copy about-copy">The participants are consciously involved in sailing activities. There are responsibilities for a wide variety of tasks in daily life. A cooking and cleaning plan should help to take responsibility towards the group. The fact of steering a sailing ship alone fills many with great pride. Recurring activities on the ship require the involvement of every crew member.</p>
<div class="btn" style="left:148px;top:1335px;width:137px;height:38px">Read More</div>

<svg class="abs" style="left:0;top:1380px" width="1200" height="180" viewBox="0 0 1200 180">
  <path d="M0,0 H1200 V30 C1000,20 860,60 720,85 C450,120 200,80 0,35 Z" fill="#f1f1f1"/>
  <path d="M0,35 C200,90 450,125 720,85 C460,170 170,170 0,100 Z" fill="#1b1f5e"/>
</svg>
<div class="photo" style="left:643px;top:1058px;width:447px;height:447px;border-radius:50%;background:linear-gradient(180deg,#8ec5e6 0%,#3f9ed0 40%,#2d86c0 60%,#d9e6ea 85%)" role="img" aria-label="Two friends sitting by the sea, one in a wheelchair, arm around each other"></div>

<!-- sponsors -->
<h2 class="abs heading sponsors-title">Our <span class="accent">Sponsors</span></h2>
<p class="abs sponsors-sub">Thank you for your great commitment and support:</p>
<div class="ship-label" style="left:166px">Ship sponsorship</div>
<div class="ship-label" style="left:460px">Ship sponsorship</div>
<div class="ship-label" style="left:766px">Ship sponsorship</div>

<div class="sponsor-card" style="left:150px;top:1815px">Nordmann</div>
<div class="sponsor-card" style="left:458px;top:1815px">Seewald</div>
<div class="sponsor-card" style="left:766px;top:1815px">Elektro Brandner</div>
<div class="sponsor-card" style="left:194px;top:1973px">Fenster Kolbe</div>
<div class="sponsor-card" style="left:502px;top:1973px">Lindtal</div>
<div class="sponsor-card" style="left:810px;top:1973px;flex-direction:column;line-height:32px">Marevo<span style="font-size:20px">www.marevo-example.at</span></div>

<svg class="arrow" style="left:120px" viewBox="0 0 48 24"><path d="M46,12 H3 M13,2 L3,12 L13,22" fill="none" stroke="#222" stroke-width="2"/></svg>
<svg class="arrow" style="left:1110px" viewBox="0 0 48 24"><path d="M2,12 H45 M35,2 L45,12 L35,22" fill="none" stroke="#222" stroke-width="2"/></svg>
<div class="btn" style="left:532px;top:2140px;width:136px;height:38px">View All</div>

<!-- cruises -->
<svg class="abs" style="left:0;top:2280px" width="1200" height="910" viewBox="0 0 1200 910">
  <path d="M0,105 C200,20 320,0 500,15 C800,40 1000,120 1200,140 V768 C1000,830 850,880 600,890 C350,900 150,880 0,900 Z" fill="#e3f4f5"/>
</svg>
<div class="photo" style="left:32px;top:2408px;width:290px;height:344px;border-radius:20px;background:linear-gradient(180deg,#f0b56a 0%,#e8a75f 35%,#6a8fa8 60%,#2f5d7f 100%)" role="img" aria-label="Cruise ship sailing at sunset near a coastline"></div>
<div class="photo" style="left:30px;top:2778px;width:288px;height:342px;border-radius:20px;background:linear-gradient(180deg,#f3d8a8 0%,#c9d2cf 40%,#4d7d99 70%,#2c5a7a 100%)" role="img" aria-label="Large white cruise ship seen from above at dusk"></div>
<div class="photo" style="left:340px;top:2645px;width:290px;height:345px;border-radius:20px;background:linear-gradient(180deg,#6f7fa0 0%,#e59d6e 45%,#557b98 65%,#1f3f60 100%)" role="img" aria-label="Cruise ship on open water under an evening sky"></div>

<h2 class="abs heading cruises-title">About <span class="accent">Cruises</span></h2>
<p class="abs body-copy cruises-copy">Lorem ipsum dolor sit amet, consectetur adipiscing elit, sed do eiusmod tempor incididunt ut labore et dolore magna aliqua. Quis ipsum suspendisse ultrices gravida. Risus commodo viverra maecenas accumsan lacus vel facilisis.</p>
<ul class="feature-list">
  <li><svg viewBox="0 0 36 30"><circle cx="14" cy="16" r="12" fill="#0f8fd0"/><path d="M7,16 L13,22 L33,3" fill="none" stroke="#1b1f5e" stroke-width="4.5" stroke-linecap="round"/></svg>Lorem ipsum dolor sit amet,</li>
  <li><svg viewBox="0 0 36 30"><circle cx="14" cy="16" r="12" fill="#0f8fd0"/><path d="M7,16 L13,22 L33,3" fill="none" stroke="#1b1f5e" stroke-width="4.5" stroke-linecap="round"/></svg>Sconsectetur adipiscing elit,</li>
  <li><svg viewBox="0 0 36 30"><circle cx="14" cy="16" r="12" fill="#0f8fd0"/><path d="M7,16 L13,22 L33,3" fill="none" stroke="#1b1f5e" stroke-width="4.5" stroke-linecap="round"/></svg>Wed do eiusmod tempor</li>
  <li><svg viewBox="0 0 36 30"><circle cx="14" cy="16" r="12" fill="#0f8fd0"/><path d="M7,16 L13,22 L33,3" fill="none" stroke="#1b1f5e" stroke-width="4.5" stroke-linecap="round"/></svg>Qcididunt ut labore et dolore</li>
  <li><svg viewBox="0 0 36 30"><circle cx="14" cy="16" r="12" fill="#0f8fd0"/><path d="M7,16 L13,22 L33,3" fill="none" stroke="#1b1f5e" stroke-width="4.5" stroke-linecap="round"/></svg>Magna aliqua. Quis ipsum</li>
  <li><svg viewBox="0 0 36 30"><circle cx="14" cy="16" r="12" fill="#0f8fd0"/><path d="M7,16 L13,22 L33,3" fill="none" stroke="#1b1f5e" stroke-width="4.5" stroke-linecap="round"/></svg>Suspendisse ultrices gravida.</li>
</ul>
<div class="btn" style="left:700px;top:2940px;width:138px;height:38px">Read More</div>

<!-- gallery -->
<h2 class="abs heading gallery-title">Gallery</h2>
<p class="abs body-copy gallery-copy">Lorem ipsum dolor sit amet, consectetur adipiscing elit, sed do eiusmod tempor incididunt ut labore et dolore magna aliqua. Quis ipsum suspendisse</p>
<div class="gallery-item" style="left:150px;top:3448px;background:linear-gradient(135deg,#d7e3e6 0%,#7fa9b8 50%,#e0894c 70%,#5d8596 100%)" role="img" aria-label="Child in a life jacket pointing from a boat"></div>
<div class="gallery-item" style="left:461px;top:3448px;background:linear-gradient(180deg,#f2f0ea 0%,#d9d5c9 40%,#e98a3a 65%,#3d6f8f 100%)" role="img" aria-label="Two children in orange life jackets in a small sailing dinghy"></div>
<div class="gallery-item" style="left:766px;top:3448px;background:linear-gradient(180deg,#7cc4e8 0%,#2f96cf 45%,#3a4fa8 65%,#e7e2d8 100%)" role="img" aria-label="Two friends by the sea, one in a wheelchair"></div>
<div class="gallery-item" style="left:150px;top:3688px;background:linear-gradient(180deg,#6d8aa0 0%,#a7b7b8 45%,#c0403a 70%,#3f5d73 100%)" role="img" aria-label="Children paddling a red kayak"></div>
<div class="gallery-item" style="left:461px;top:3688px;background:linear-gradient(180deg,#4aa3de 0%,#2f8fd0 50%,#e8eef3 60%,#1f6fb0 100%)" role="img" aria-label="Two small sailboats on bright blue water"></div>
<div class="gallery-item" style="left:766px;top:3688px;background:linear-gradient(135deg,#5aa9d8 0%,#3c8dc6 50%,#e0b592 70%,#2c5fa8 100%)" role="img" aria-label="Laughing child in a life jacket by the water"></div>
<div class="btn" style="left:532px;top:3946px;width:136px;height:38px">View All</div>

<!-- footer -->
<svg class="abs" style="left:0;top:4040px" width="1200" height="458" viewBox="0 0 1200 458" role="img" aria-label="Faded photo of two friends by the sea behind the footer">
  <path d="M0,40 C400,0 800,0 1200,60 V458 H0 Z" fill="#0f8fd0"/>
  <path d="M0,210 C300,190 500,260 800,230 C1000,210 1100,160 1200,150 V458 H0 Z" fill="#232a63"/>
  <ellipse cx="300" cy="330" rx="220" ry="160" fill="#2c3572" opacity=".6"/>
</svg>
<div class="abs footer-mark"></div>
<div class="abs footer-name">Verein Sail Buddies</div>
<nav class="abs footer-nav"><span>Home</span><span>Sponsors</span><span>Fleet Info 2022</span><span>Gallery</span><span>Cruises</span></nav>
<div class="abs copyright">2022 © Sailbuddies. All Rights are reserved.</div>

</body>
</html>
```